Torvale Wound Care Business card design

We need a business card designed around our logo which was provided. The logo of preference is the colored. Also the colors and fonts were provided.

Target Market(s)

Our Referral partners are home health agencies.

Industry/Entity Type

Healthcare

Contact Information for Business Card

Name , Phone #, Email , Title

Requirements
Nice to have
• Creativity
Should not have
• basic

```html
<!DOCTYPE html>
<html lang="en">
<head>
<meta charset="utf-8">
<title>Torvale Wound Care — Business Card</title>
<link href="https://fonts.googleapis.com/css2?family=Montserrat:wght@400;700&family=Varela+Round&display=swap" rel="stylesheet">
<style>
  :root {
    --backdrop: #0b0b0b;
    --paper: #ffffff;
    --navy: #164a87;
    --brand: #1e4f93;
    --frame: #1a5aa6;
    --frame-light: #1b8fd6;
    --back-dark: #0c5197;
    --back-light: #0279c2;
    --ink-light: #ffffff;
  }
  * { margin: 0; padding: 0; box-sizing: border-box; }
  html, body { width: 1200px; height: 2347px; overflow: hidden; background: var(--backdrop); }
  .canvas { position: relative; width: 1200px; height: 2347px; background: var(--backdrop); }

  .card { position: absolute; left: 50px; width: 1100px; height: 628px; overflow: hidden; }

  .card-front { top: 73px; background: var(--paper); }
  .front-band { position: absolute; left: 0; right: 0; top: 382px; bottom: 0; background: var(--navy); }
  .front-frame {
    position: absolute; left: 39px; top: 37px; width: 1024px; height: 553px;
    border: 3px solid var(--frame);
    border-bottom-color: var(--frame-light);
  }
  .front-frame::after {
    content: ""; position: absolute; left: -3px; right: -3px; top: 345px; bottom: -3px;
    border: 3px solid var(--frame-light); border-top: none;
  }

  .wordmark {
    position: absolute; left: 0; right: 0; display: flex; align-items: center; justify-content: center;
    font-family: "Montserrat", sans-serif; font-weight: 700; white-space: nowrap; line-height: 1;
  }
  .wordmark-dot { border-radius: 50%; flex: none; }

  .card-front .wordmark { top: 182px; gap: 18px; font-size: 50px; color: var(--brand); }
  .card-front .wordmark-dot { width: 46px; height: 46px; background: var(--brand); }

  .contact-list {
    position: absolute; left: 84px; top: 400px; list-style: none;
    font-family: "Varela Round", sans-serif; font-size: 26px; letter-spacing: 1px; color: var(--ink-light);
  }
  .contact-list li { display: flex; align-items: center; gap: 8px; height: 39px; }
  .contact-list svg { width: 22px; height: 22px; flex: none; }

  .holder { position: absolute; right: 76px; top: 404px; text-align: right; color: var(--ink-light); font-family: "Montserrat", sans-serif; }
  .holder-name { font-size: 31px; line-height: 1.1; font-weight: 400; letter-spacing: .5px; }
  .holder-name strong { font-weight: 700; }
  .holder-title { font-size: 23px; line-height: 1.2; }

  .card-back { top: 754px; background: linear-gradient(215deg, var(--back-light) 0%, var(--back-dark) 70%); }
  .card-back .wordmark { top: 282px; gap: 24px; font-size: 66px; color: var(--ink-light); }
  .card-back .wordmark-dot { width: 62px; height: 62px; background: var(--ink-light); }
</style>
</head>
<body>
<main class="canvas">

  <section class="card card-front" aria-label="Business card front">
    <div class="front-band"></div>
    <div class="front-frame"></div>

    <div class="wordmark">
      <span class="wordmark-dot"></span>
      <span class="wordmark-name">Torvale Wound Care</span>
    </div>

    <ul class="contact-list">
      <li>
        <svg viewBox="0 0 22 22" aria-hidden="true"><circle cx="11" cy="11" r="10" fill="#fff"/><rect x="5.5" y="7" width="11" height="8" rx="1" fill="none" stroke="#164a87" stroke-width="1.6"/><path d="M5.8 7.5 11 11.5l5.2-4" fill="none" stroke="#164a87" stroke-width="1.6"/></svg>
        urname@email.com
      </li>
      <li>
        <svg viewBox="0 0 22 22" aria-hidden="true"><circle cx="11" cy="11" r="10" fill="#fff"/><circle cx="11" cy="11" r="6" fill="none" stroke="#164a87" stroke-width="1.4"/><path d="M5 11h12M11 5c-3 3-3 9 0 12M11 5c3 3 3 9 0 12" fill="none" stroke="#164a87" stroke-width="1.2"/></svg>
        www.yourwebsite.com
      </li>
      <li>
        <svg viewBox="0 0 22 22" aria-hidden="true"><circle cx="11" cy="11" r="10" fill="#fff"/><path d="M8 6.5c-1.5 1-2 3 -.5 5.5s4 4.5 6 4.5c1.2 0 2-.8 2.3-1.5l-2.3-1.6-1.2 1c-1.2-.6-2.6-2-3.2-3.3l1-1.1L8.6 6.3z" fill="#164a87"/></svg>
        +000 12345 6789
      </li>
    </ul>

    <div class="holder">
      <p class="holder-name"><strong>DALEN</strong> MORROW</p>
      <p class="holder-title">Director</p>
    </div>
  </section>

  <section class="card card-back" aria-label="Business card back">
    <div class="wordmark">
      <span class="wordmark-dot"></span>
      <span class="wordmark-name">Torvale Wound Care</span>
    </div>
  </section>

</main>
</body>
</html>
```